Christmas social media advert post

I am looking for an eye catching advert for use mainly on social media posts.
The following is the detail of the event.

Christmas special offer-
£10pp,– offer includes –
Half an hour Toboggan track,
Half an hour Slingshot paintballs (20 paintballs pp) and safe target archery (under cover and indoor ranges). Activities all the family from age 4 to grandparents can join in,
Also available – Add on indoor activities including Mini Curling, Bead Blitz, Safe axe throwing, Air juggler – from £3.50pp and age 6plus
Café open for hot food and drinks in the ‘Fireside Frost Lodge and the heated Christmas marquee.

A basic idea I put together for what I feel is the important information is -

Christmas Special offer -
Starts Saturday 20th December.
£10pp – offer includes –
Half an hour Slingshot paintballs (20 paintballs pp) and safe target archery (under cover and indoor ranges). Activities all the family from age 4 to grandparents can join in. Booking is essential - details on how below.
Also available Add on indoor activities - including Mini Curling, Bead Blitz, Safe axe throwing, Air juggler – from £3.50pp and age 6plus.
Ages start from 4 plus.
All activities are great for children and adults so perfect for families as well as friends, parties and get togethers.
Free huge car parks,
Booking is easy-
Just Message from Parlo chat (on this post) or email
martin@hollowbrookleisurepark.co.uk for availability of your preferred date and time.

I would be happy to send the detailed information to enquiries if it meant a better looking advert / post.

Full details are in the picture uploads, feel free to use as much or as little of the information as you feel best.

```html
<!DOCTYPE html>
<html lang="en">
<head>
<meta charset="utf-8">
<title>Christmas Special Offer</title>
<link href="https://fonts.googleapis.com/css2?family=Playfair+Display:wght@400;500&family=Montserrat:wght@400;500;700&family=Roboto+Condensed:wght@400;500&family=Pacifico&display=swap" rel="stylesheet">
<style>
  :root {
    --red: #c0281f;
    --red-dark: #a81d16;
    --ink: #1f1f1f;
    --paper: #f6f6f6;
    --white: #ffffff;
    --frost: #e4e4e6;
  }
  * { margin: 0; padding: 0; box-sizing: border-box; }
  html, body { width: 1200px; height: 1200px; overflow: hidden; background: var(--paper); }
  .advert {
    position: relative; width: 1200px; height: 1200px; overflow: hidden;
    background: linear-gradient(180deg, #f2f2f2 0%, #fafafa 60%, #ffffff 100%);
    color: var(--ink);
    font-family: "Montserrat", sans-serif;
  }
  .photo { position: absolute; }
  .photo-tree-top {
    left: 0; top: 0; width: 500px; height: 641px;
    background: linear-gradient(135deg, #d4cfcd 0%, #c7a8a6 40%, #e6e2e1 70%, rgba(246,246,246,0) 100%);
  }
  .photo-tree-bottom {
    right: 0; top: 830px; width: 340px; height: 370px;
    background: linear-gradient(250deg, #d2b4b2 0%, #e4dedd 50%, rgba(255,255,255,0) 100%);
  }
  .headline { position: absolute; }
  .title-christmas {
    left: 420px; top: 20px; width: 720px; text-align: center;
    font-family: "Playfair Display", serif; font-weight: 400;
    font-size: 158px; line-height: 1; color: var(--red);
  }
  .title-special {
    left: 486px; top: 168px;
    font-family: "Playfair Display", serif; font-weight: 400;
    font-size: 120px; line-height: 1; color: var(--ink);
  }
  .title-offer {
    left: 893px; top: 172px;
    font-family: "Pacifico", cursive; font-size: 80px; line-height: 1; color: var(--ink);
  }
  .rule { position: absolute; height: 2px; background: var(--ink); }
  .rule-left { left: 388px; top: 238px; width: 82px; }
  .rule-right { left: 1076px; top: 238px; width: 82px; }
  .rule-date-top { left: 481px; top: 312px; width: 609px; }
  .rule-date-bottom { left: 481px; top: 383px; width: 609px; }
  .start-date {
    position: absolute; left: 435px; width: 700px; top: 320px; text-align: center;
    font-family: "Playfair Display", serif; font-size: 46px; line-height: 1.1; color: var(--ink);
  }
  .start-date em { font-style: normal; color: var(--red); }
  .price-box {
    position: absolute; left: 578px; top: 407px; width: 461px; height: 66px;
    border: 2px solid var(--red); background: var(--white); display: flex; align-items: center;
  }
  .price-tag {
    height: 100%; width: 172px; background: var(--red); color: var(--white);
    clip-path: polygon(0 0, 100% 0, 90% 100%, 0 100%);
    font-weight: 700; font-size: 44px; display: flex; align-items: center; padding-left: 14px;
    letter-spacing: -1px;
  }
  .price-label { font-size: 38px; font-weight: 500; margin-left: 6px; color: var(--ink); }
  .offer-main {
    position: absolute; left: 540px; width: 532px; top: 484px; text-align: center;
    font-size: 34px; font-weight: 400; color: var(--ink);
  }
  .rule-short { left: 740px; top: 544px; width: 134px; }
  .offer-detail {
    position: absolute; left: 460px; width: 720px; top: 560px; text-align: center;
    font-size: 21.5px; line-height: 27px; color: var(--ink);
  }
  .offer-detail strong { font-weight: 700; }
  .activity-strip {
    position: absolute; left: 0; top: 641px; width: 1200px; height: 189px;
    display: flex; gap: 3px; background: var(--white);
  }
  .activity-strip .photo { position: static; flex: 1; height: 100%; }
  .ph-cabin { background: linear-gradient(160deg, #6b4a2c, #b08660 55%, #d8c3a8); }
  .ph-archery { background: linear-gradient(180deg, #d9dcd8, #9ea19c 55%, #6f716e); }
  .ph-curling { background: linear-gradient(170deg, #6d7e5d, #c5a77a 45%, #d9bb8c); }
  .ph-paintball { background: linear-gradient(160deg, #3a4a34, #2a1f4a 50%, #4b3560); }
  .ph-axe { background: linear-gradient(150deg, #8c7a5c, #2141a6 40%, #c7282c 70%, #e6c84a); }
  .info-box {
    position: absolute; left: 50px; width: 816px; border: 1.5px solid #555; background: var(--white);
    font-family: "Roboto Condensed", sans-serif; font-size: 24.5px; line-height: 27px;
    padding: 6px 28px; color: var(--ink);
  }
  .info-box em { font-style: normal; color: var(--red); }
  .info-addons { top: 851px; height: 78px; padding-top: 10px; }
  .info-cafe { top: 939px; height: 62px; padding-top: 4px; }
  .family-line {
    position: absolute; left: 53px; top: 1016px;
    font-family: "Roboto Condensed", sans-serif; font-weight: 500; font-size: 28px; color: var(--ink);
  }
  .family-line em { font-style: normal; color: var(--red); }
  .booking-band {
    position: absolute; left: 0; top: 1060px; width: 1200px; height: 140px;
    background: linear-gradient(90deg, var(--red-dark) 0%, var(--red) 55%, rgba(192,40,31,0.85) 72%, rgba(192,40,31,0) 88%);
  }
  .booking-text {
    position: absolute; left: 50px; top: 1071px; padding-left: 11px;
    border-left: 2px solid var(--white); color: var(--white);
    font-size: 23.5px; line-height: 26.5px;
  }
  .booking-text strong { font-weight: 700; }
</style>
</head>
<body>
<main class="advert">
  <div class="photo photo-tree-top" role="img" aria-label="White Christmas tree with red heart and bauble ornaments and silver snowflakes"></div>
  <div class="photo photo-tree-bottom" role="img" aria-label="White Christmas tree branch with red heart bauble"></div>

  <h1 class="headline title-christmas">Christmas</h1>
  <div class="rule rule-left"></div>
  <div class="headline title-special">Special</div>
  <div class="headline title-offer">offer</div>
  <div class="rule rule-right"></div>

  <div class="rule rule-date-top"></div>
  <p class="start-date">Starts Saturday <em>20th</em> December</p>
  <div class="rule rule-date-bottom"></div>

  <div class="price-box">
    <span class="price-tag">£10pp</span>
    <span class="price-label">offer includes</span>
  </div>
  <p class="offer-main">Half An Hour Toboggan Track</p>
  <div class="rule rule-short"></div>
  <p class="offer-detail"><strong>Half an hour Slingshot paintballs</strong> (20 paintballs pp) and<br>safe target archery (under cover and indoor ranges).</p>

  <div class="activity-strip">
    <div class="photo ph-cabin" role="img" aria-label="Cosy wooden cabin with log burner and hot chocolates"></div>
    <div class="photo ph-archery" role="img" aria-label="Indoor archery range with targets"></div>
    <div class="photo ph-curling" role="img" aria-label="Mini curling on a wooden lane"></div>
    <div class="photo ph-paintball" role="img" aria-label="Slingshot paintball range with coloured lights"></div>
    <div class="photo ph-axe" role="img" aria-label="Safe axe throwing target board"></div>
  </div>

  <div class="info-box info-addons">Also available Add on indoor activities - including Mini Curling, Bead Blitz, Safe axe throwing, Air juggler – from <em>£3.50pp</em> and age 6plus.</div>
  <div class="info-box info-cafe">Café open for hot food and drinks in the ‘Fireside Frost Lodge and the heated Christmas marquee.</div>

  <p class="family-line"><em>Activities all the family from</em> age 4 to grandparents <em>can join in,</em></p>

  <div class="booking-band"></div>
  <p class="booking-text"><strong>Free huge car parks, Booking is easy-</strong><br>Just Message from <strong>Parlo chat</strong> (on this post) or email<br><strong>martin@hollowbrookleisurepark.co.uk</strong> for availability of<br>your preferred date and time.</p>
</main>
</body>
</html>
```